Business Card *

A business card design
Use the logo uploaded in the brief page.
You may use placeholders in your design layouts.
I will provide the actual business card details to the winning designer.

Logo
Place for contact info (name, title, phone, email, etc)

Requirements
Must have
• Logo

```html
<!DOCTYPE html>
<html lang="en">
<head>
<meta charset="utf-8">
<title>Harrowfield Business Card</title>
<link rel="stylesheet" href="https://fonts.googleapis.com/css2?family=Arimo:wght@400;700&display=swap">
<style>
  :root {
    --frame-blue: #1f77c4;
    --sheet: #ffffff;
    --card-black: #000000;
    --ink: #111111;
    --brand-grey: #8a8a8a;
    --brand-green: #49b947;
    --pattern-grey: #4a4a4a;
    --white: #ffffff;
  }
  * { box-sizing: border-box; margin: 0; padding: 0; }
  html, body { width: 966px; height: 1200px; overflow: hidden; background: var(--sheet); }
  body { font-family: "Arimo", Arial, sans-serif; color: var(--ink); }

  .sheet {
    position: relative; width: 966px; height: 1200px;
    border: 9px solid var(--frame-blue); background: var(--sheet);
  }

  .card { position: absolute; left: 57px; width: 835px; }
  .card-front { top: 31px; height: 531px; background: var(--card-black); overflow: hidden; }
  .card-back { top: 616px; height: 530px; background: var(--white); border: 1.5px solid var(--ink); }

  /* faint repeated brand marks */
  .brand-tile {
    position: absolute; width: 110px; margin-left: -55px;
    display: flex; flex-direction: column; align-items: center; gap: 4px;
  }
  .brand-tile .dot { width: 28px; height: 28px; border-radius: 50%; background: var(--pattern-grey); }
  .brand-tile .word { font-weight: 700; font-size: 11px; color: var(--pattern-grey); letter-spacing: 0.2px; }

  /* main brand lockup */
  .brand {
    position: absolute; display: flex; flex-direction: column; align-items: center;
  }
  .brand .dot { border-radius: 50%; }
  .brand .word { font-weight: 700; letter-spacing: 0.5px; line-height: 1; }
  .brand .tagline { font-weight: 700; letter-spacing: 2px; line-height: 1; }

  .brand-front { left: 417px; top: 190px; width: 280px; margin-left: -140px; }
  .brand-front .dot { width: 86px; height: 86px; background: var(--white); margin-bottom: 14px; }
  .brand-front .word { font-size: 30px; color: var(--white); }
  .brand-front .tagline { font-size: 11px; color: var(--white); margin-top: 6px; }

  .brand-back { left: 66px; top: 185px; width: 272px; }
  .brand-back .dot { width: 112px; height: 112px; background: var(--brand-grey); margin-bottom: 14px; }
  .brand-back .word { font-size: 34px; color: var(--brand-grey); }
  .brand-back .tagline { font-size: 12px; color: var(--brand-grey); margin-top: 6px; }

  /* person + contact */
  .person { position: absolute; right: 51px; top: 78px; text-align: right; }
  .person-name { font-weight: 700; font-size: 26px; letter-spacing: 0.5px; }
  .person-title { font-size: 19px; margin-top: 8px; }

  .contact-list { position: absolute; right: 40px; top: 250px; list-style: none; }
  .contact-item {
    display: flex; justify-content: flex-end; align-items: center;
    font-size: 23px; height: 38px;
  }
  .contact-item:first-child { margin-bottom: 6px; }
  .contact-item svg { width: 24px; height: 24px; margin-left: 18px; flex: none; }
</style>
</head>
<body>
<main class="sheet">

  <section class="card card-front" aria-label="Card front">
    <div class="brand-tile" style="left:70px;top:70px"><span class="dot"></span><span class="word">HARROWFIELD</span></div>
    <div class="brand-tile" style="left:204px;top:70px"><span class="dot"></span><span class="word">HARROWFIELD</span></div>
    <div class="brand-tile" style="left:337px;top:70px"><span class="dot"></span><span class="word">HARROWFIELD</span></div>
    <div class="brand-tile" style="left:472px;top:70px"><span class="dot"></span><span class="word">HARROWFIELD</span></div>
    <div class="brand-tile" style="left:607px;top:70px"><span class="dot"></span><span class="word">HARROWFIELD</span></div>
    <div class="brand-tile" style="left:741px;top:70px"><span class="dot"></span><span class="word">HARROWFIELD</span></div>

    <div class="brand-tile" style="left:70px;top:252px"><span class="dot"></span><span class="word">HARROWFIELD</span></div>
    <div class="brand-tile" style="left:204px;top:252px"><span class="dot"></span><span class="word">HARROWFIELD</span></div>
    <div class="brand-tile" style="left:607px;top:252px"><span class="dot"></span><span class="word">HARROWFIELD</span></div>
    <div class="brand-tile" style="left:741px;top:252px"><span class="dot"></span><span class="word">HARROWFIELD</span></div>

    <div class="brand-tile" style="left:70px;top:452px"><span class="dot"></span><span class="word">HARROWFIELD</span></div>
    <div class="brand-tile" style="left:204px;top:452px"><span class="dot"></span><span class="word">HARROWFIELD</span></div>
    <div class="brand-tile" style="left:337px;top:452px"><span class="dot"></span><span class="word">HARROWFIELD</span></div>
    <div class="brand-tile" style="left:472px;top:452px"><span class="dot"></span><span class="word">HARROWFIELD</span></div>
    <div class="brand-tile" style="left:607px;top:452px"><span class="dot"></span><span class="word">HARROWFIELD</span></div>
    <div class="brand-tile" style="left:741px;top:452px"><span class="dot"></span><span class="word">HARROWFIELD</span></div>

    <div class="brand brand-front">
      <span class="dot"></span>
      <span class="word">HARROWFIELD</span>
      <span class="tagline">AGRICULTURE AND INDUSTRY</span>
    </div>
  </section>

  <section class="card card-back" aria-label="Card back">
    <div class="brand brand-back">
      <span class="dot"></span>
      <span class="word">HARROWFIELD</span>
      <span class="tagline">AGRICULTURE AND INDUSTRY</span>
    </div>

    <div class="person">
      <p class="person-name">DR ALEX MARLOW</p>
      <p class="person-title">Technology Specialist</p>
    </div>

    <ul class="contact-list">
      <li class="contact-item">Your addressIt needs to have
        <svg viewBox="0 0 24 24" aria-hidden="true"><path d="M3 2 L21 12 L13 14 L9 22 Z" fill="#111"/></svg>
      </li>
      <li class="contact-item">1300 555 014
        <svg viewBox="0 0 24 24" aria-hidden="true"><rect x="6" y="2" width="12" height="20" rx="2" fill="none" stroke="#111" stroke-width="2"/><rect x="9" y="5" width="6" height="5" fill="#111"/><circle cx="10" cy="14" r="1" fill="#111"/><circle cx="14" cy="14" r="1" fill="#111"/><circle cx="10" cy="18" r="1" fill="#111"/><circle cx="14" cy="18" r="1" fill="#111"/></svg>
      </li>
      <li class="contact-item">info@drmarlow.com
        <svg viewBox="0 0 24 24" aria-hidden="true"><rect x="3" y="6" width="18" height="13" fill="#111"/><path d="M3 6 L12 13 L21 6" fill="none" stroke="#fff" stroke-width="1.6"/></svg>
      </li>
      <li class="contact-item">www.drmarlow.com
        <svg viewBox="0 0 24 24" aria-hidden="true"><g fill="none" stroke="#111" stroke-width="2.6" stroke-linecap="round"><path d="M10 14 L7 17 a3 3 0 0 1 -4 -4 L7 9 a3 3 0 0 1 4 0"/><path d="M14 10 L17 7 a3 3 0 0 1 4 4 L17 15 a3 3 0 0 1 -4 0"/><path d="M9.5 14.5 L14.5 9.5"/></g></svg>
      </li>
    </ul>
  </section>

</main>
</body>
</html>
```